Velmora Partners - website for real estate investment company

Create a bold, modern website that reflects Velmora’s success, professionalism, and credibility.
The design must stand out while maintaining a polished, corporate tone. (bold, but understated)
The client just created a new logo, and the website design must be in sync with the logo design. Information about the logo colors, fonts, and message are in the attached design brief.
Updates

Target Market(s)

b2b: banks, brokers, institutional partners, vendors, and property sellers.

Industry/Entity Type

real estate investment company

Number of Pages Required

1 page

Font styles to use
Sans Serif

Colors

Designer to choose colors to be used in the design.

Requirements
Must have
• 1. homepage design (psd) 2. a top banner image (psd) for a default inner page
Nice to have
• please see attached design brief
Should not have

```html
<!DOCTYPE html>
<html lang="en">
<head>
<meta charset="UTF-8">
<title>Velmora Partners</title>
<link href="https://fonts.googleapis.com/css2?family=Inter:wght@400;500;600;700&family=Red+Hat+Display:wght@400;500;600;700;800&display=swap" rel="stylesheet">
<style>
:root{
  --red:#dd2a27;
  --ink:#1d1d1d;
  --muted:#555;
  --cream:#f8f5f0;
  --pink:#ffc9c9;
  --grey:#f2f2f2;
  --black:#000;
  --white:#fff;
  --line:#cfcfcf;
}
*{box-sizing:border-box;margin:0;padding:0}
html,body{width:1200px;height:4000px;overflow:hidden}
body{position:relative;background:var(--white);font-family:"Red Hat Display",sans-serif;color:var(--ink)}
.abs{position:absolute}
/* nav */
.site-nav{position:absolute;left:0;top:0;width:1200px;height:98px;background:var(--white)}
.brand{position:absolute;left:34px;top:26px;font-family:"Inter",sans-serif;font-weight:800;font-size:31px;letter-spacing:1px;color:#3a3a3a}
.nav-links{position:absolute;top:33px;left:0;width:1200px;font-family:"Inter",sans-serif;font-size:13px;color:var(--ink)}
.nav-links span{position:absolute}
/* hero */
.hero{position:absolute;left:0;top:98px;width:1200px;height:406px;background:linear-gradient(180deg,#1f3a5e 0%,#4d78a8 45%,#9cc2e6 70%,#2a4a70 100%)}
.hero-title{position:absolute;top:284px;width:1200px;text-align:center;font-family:"Inter",sans-serif;font-weight:700;font-size:39px;color:#111}
.btn{position:absolute;background:var(--red);color:var(--white);display:flex;align-items:center;justify-content:center;gap:10px;font-family:"Inter",sans-serif;font-size:20px}
/* stats */
.stat-icon{position:absolute;width:40px;height:40px}
.stat-label{position:absolute;font-family:"Inter",sans-serif;font-size:19px;line-height:24px;color:var(--ink)}
.stat-num{position:absolute;font-family:"Inter",sans-serif;font-weight:700;font-size:33px;color:var(--red)}
/* about */
.brand-panel{position:absolute;left:133px;top:765px;width:326px;height:404px;background:var(--red)}
.about-text{position:absolute;left:551px;top:820px;width:490px;font-family:"Inter",sans-serif;font-size:20px;line-height:37px;color:#222}
/* who */
.who{position:absolute;left:0;top:1238px;width:1200px;height:851px;background:var(--cream)}
.sec-title{position:absolute;width:1200px;text-align:center;font-weight:700;font-size:40px;color:var(--ink)}
.who-sub{position:absolute;top:162px;width:1200px;text-align:center;font-size:15px;line-height:24px;color:#444}
.tile{position:absolute;top:255px;width:224px;height:324px}
.tile-label{position:absolute;top:600px;font-size:19px;font-weight:500;color:var(--ink)}
/* reviews */
.reviews{position:absolute;left:0;top:2089px;width:1200px;height:587px;background:var(--pink);overflow:hidden}
.card{position:absolute;top:140px;width:296px;height:391px;background:var(--white);border-radius:10px;overflow:hidden}
.card-photo{position:absolute;left:0;top:0;width:100%;height:188px}
.card-text{position:absolute;left:22px;top:220px;width:255px;font-size:14.5px;line-height:24px;color:#222}
.card-name{position:absolute;left:22px;top:328px;font-size:15px;font-weight:500;color:#222}
.card-role{position:absolute;left:22px;top:351px;font-size:12.5px;color:#666}
.arrow{position:absolute;top:2303px;width:46px;height:46px;border-radius:50%;background:var(--red);display:flex;align-items:center;justify-content:center}
/* footer */
.footer{position:absolute;left:0;top:3225px;width:1200px;height:775px;background:var(--black);color:var(--white)}
/* contact */
.contact{position:absolute;left:115px;top:2742px;width:953px;height:540px;background:var(--grey)}
.field{position:absolute;background:var(--white);border:1px solid #bdbdbd;border-radius:5px;font-size:13px;color:#666;padding:0 18px;display:flex;align-items:center;justify-content:space-between}
.foot-head{position:absolute;font-size:20px;font-weight:500}
.foot-link{position:absolute;font-size:13px;color:#ddd}
.social{position:absolute;top:3813px;width:30px;height:30px;border:1.5px solid var(--white);border-radius:50%}
</style>
</head>
<body>

<header class="site-nav">
  <div class="brand">VELMORA</div>
  <nav class="nav-links">
    <span style="left:309px">Home</span>
    <span style="left:419px">Our Story</span>
    <span style="left:551px">Investment Strategy</span>
    <span style="left:747px">What Sets Us Apart</span>
    <span style="left:940px">Our Portfolio</span>
    <span style="left:1091px">Contact</span>
  </nav>
</header>

<section class="hero" role="img" aria-label="Upward view of glass skyscrapers against a blue sky">
  <h1 class="hero-title" style="top:186px">Experience. Strategy. Vision</h1>
  <div class="btn" style="left:490px;top:262px;width:219px;height:51px">Learn More
    <svg width="16" height="14" viewBox="0 0 16 14"><path d="M1 7h13M9 2l5 5-5 5" stroke="#fff" stroke-width="1.6" fill="none"/></svg></div>
</section>

<section class="stats">
  <svg class="stat-icon" style="left:209px;top:576px" viewBox="0 0 40 40" fill="none" stroke="#9a9a9a" stroke-width="2"><rect x="3" y="4" width="34" height="32" rx="3"/><path d="M3 14h34M3 25h34M15 4v10M25 14v11M15 25v11"/></svg>
  <div class="stat-label" style="left:265px;top:564px">Founded</div>
  <div class="stat-num" style="left:265px;top:586px">1989</div>

  <svg class="stat-icon" style="left:427px;top:574px;width:44px;height:44px" viewBox="0 0 44 44" fill="none" stroke="#9a9a9a" stroke-width="2"><rect x="8" y="6" width="28" height="34"/><path d="M2 40h40M22 11v10M17 16h10M14 27h5M25 27h5M14 33h5M25 33h5"/></svg>
  <div class="stat-num" style="left:486px;top:553px">23000+</div>
  <div class="stat-label" style="left:486px;top:592px">multifamily &amp;<br>healthcare units</div>

  <svg class="stat-icon" style="left:759px;top:576px" viewBox="0 0 40 40" fill="none" stroke="#9a9a9a" stroke-width="2"><path d="M3 37V17h10v20M13 37V4h24v33M2 37h36M19 11h3M28 11h3M19 19h3M28 19h3M19 27h3M28 27h3M7 23h2M7 30h2"/></svg>
  <div class="stat-num" style="left:816px;top:563px">$300 Million+</div>
  <div class="stat-label" style="left:816px;top:603px">invested in renovations</div>
</section>

<section class="about">
  <div class="brand-panel" role="img" aria-label="Velmora brand colour panel"></div>
  <p class="about-text">Velmora Partners is a vertically integrated real estate investment firm with a proven four-decade track record. We acquire, reposition, and operate high-performing assets across multiple sectors — always with a focus on exceptional, risk-adjusted returns.</p>
  <div class="btn" style="left:551px;top:1032px;width:220px;height:53px">Learn More
    <svg width="16" height="14" viewBox="0 0 16 14"><path d="M1 7h13M9 2l5 5-5 5" stroke="#fff" stroke-width="1.6" fill="none"/></svg></div>
</section>

<section class="who">
  <h2 class="sec-title" style="top:97px">Who We Work With</h2>
  <p class="who-sub">Our success through many market cycles is made possible by the continued loyalty<br>and trust of our investors</p>
  <div class="tile" style="left:132px;background:linear-gradient(180deg,#b9b79a,#6f8a4d 60%,#46652d)" role="img" aria-label="Aerial view of a suburban neighbourhood"></div>
  <div class="tile" style="left:369px;background:linear-gradient(160deg,#2d3a55,#8a8e93 55%,#cfd2d0)" role="img" aria-label="Brokers with a model of apartment buildings"></div>
  <div class="tile" style="left:606px;background:linear-gradient(180deg,#1e55b8,#6b93d4 45%,#8a7a60 80%,#3b3528)" role="img" aria-label="City towers along a waterfront"></div>
  <div class="tile" style="left:843px;background:linear-gradient(180deg,#2a6bc9,#8fb6e8 40%,#d9cf9c 70%,#f0efe8)" role="img" aria-label="Bank building facade with columns"></div>
  <div class="tile-label" style="left:132px">Property Sellers</div>
  <div class="tile-label" style="left:369px">Investment Brokers</div>
  <div class="tile-label" style="left:606px">Institutional Partners</div>
  <div class="tile-label" style="left:843px">Mortgage Banks</div>
  <div class="btn" style="left:473px;top:691px;width:253px;height:64px;border-radius:3px;font-family:'Red Hat Display',sans-serif;font-weight:700;font-size:20px">View All Services</div>
</section>

<section class="reviews">
  <h2 class="sec-title" style="top:48px;font-size:38px">Customer Reviews</h2>
  <div class="card" style="left:-212px">
    <div class="card-photo" style="background:linear-gradient(180deg,#8fa0b0,#3b4450)" role="img" aria-label="Reviewer portrait"></div>
    <p class="card-text">We were glad we did a short-term trial, and it was very helpful to us. We will book again!</p>
    <div class="card-name">Owen Reid</div><div class="card-role">Property Owner</div>
  </div>
  <div class="card" style="left:108px">
    <div class="card-photo" style="background:linear-gradient(180deg,#d9d2c6,#a89a88)" role="img" aria-label="Reviewer working at a laptop"></div>
    <p class="card-text">We absolutely appreciate working with Brightkeep Services! Our clients continue to request them week by week.</p>
    <div class="card-name">Daren Colt</div><div class="card-role">Vacation Rental Investor</div>
  </div>
  <div class="card" style="left:428px">
    <div class="card-photo" style="background:linear-gradient(180deg,#cfc4b4,#8a3a48)" role="img" aria-label="Reviewer at a desk with a laptop"></div>
    <p class="card-text">"Great service, great value and always available to help. They go above and beyond regularly - great partner for short-stay cleans."</p>
    <div class="card-name">Leon Marsh</div><div class="card-role">VP Business Development</div>
  </div>
  <div class="card" style="left:748px">
    <div class="card-photo" style="background:linear-gradient(180deg,#7a8a5a,#c99a5a)" role="img" aria-label="Reviewer standing in an office"></div>
    <p class="card-text">They are always on time, answer their phones and I've never had a guest complain about their work and have never been let down.</p>
    <div class="card-name">Ravi Trent</div><div class="card-role">Real Estate Broker</div>
  </div>
  <div class="card" style="left:1068px">
    <div class="card-photo" style="background:linear-gradient(180deg,#9fb2b6,#3a4a55)" role="img" aria-label="Reviewer portrait"></div>
    <p class="card-text">I had the pleasure of working with Brightkeep Services. Their teams are always reliable.</p>
    <div class="card-name">Owen Pike</div><div class="card-role">Vacation Rental Investor</div>
  </div>
</section>
<div class="arrow" style="left:61px"><svg width="22" height="18" viewBox="0 0 22 18"><path d="M21 9H3M10 2L3 9l7 7" stroke="#fff" stroke-width="2.2" fill="none"/></svg></div>
<div class="arrow" style="left:1117px"><svg width="22" height="18" viewBox="0 0 22 18"><path d="M1 9h18M12 2l7 7-7 7" stroke="#fff" stroke-width="2.2" fill="none"/></svg></div>

<footer class="footer">
  <h2 class="abs" style="left:132px;top:115px;font-size:37px;font-weight:700;line-height:50px">Get The Latest<br>Updates</h2>
  <div class="field" style="left:495px;top:110px;width:369px;height:64px;background:transparent;border-color:#bbb;color:#ddd">Enter your email</div>
  <div class="abs" style="left:878px;top:110px;width:190px;height:64px;background:var(--white);color:#000;border-radius:3px;display:flex;align-items:center;justify-content:center;font-size:20px;font-weight:700">Subscribe</div>
  <div class="abs" style="left:132px;top:237px;width:936px;height:1px;background:#444"></div>

  <div class="foot-head" style="left:132px;top:308px">Services</div>
  <div class="foot-link" style="left:132px;top:357px">Mortgage Auditing</div>
  <div class="foot-link" style="left:132px;top:394px">Investment</div>
  <div class="foot-link" style="left:132px;top:431px">Real Estate Consultant</div>

  <div class="foot-head" style="left:379px;top:308px">About Us</div>
  <div class="foot-link" style="left:379px;top:357px;text-decoration:underline">Home</div>
  <div class="foot-link" style="left:379px;top:394px">Projects</div>
  <div class="foot-link" style="left:379px;top:431px">Career</div>
  <div class="foot-link" style="left:379px;top:468px">About Us</div>
  <div class="foot-link" style="left:379px;top:505px">Blog</div>

  <div class="foot-head" style="left:574px;top:308px">Resource</div>
  <div class="foot-link" style="left:574px;top:357px">Contact Us</div>
  <div class="foot-link" style="left:574px;top:394px">Terms</div>
  <div class="foot-link" style="left:574px;top:431px">Policy</div>
  <div class="foot-link" style="left:574px;top:468px">Payments</div>

  <div class="abs" style="left:790px;top:300px;font-size:56px;font-weight:800;letter-spacing:2px">VELMORA</div>
  <div class="foot-link" style="left:790px;top:402px">Office</div>
  <div class="abs" style="left:790px;top:430px;font-size:28px;font-weight:700">Ashford, NJ</div>

  <svg class="abs" style="left:132px;top:589px" width="28" height="28" viewBox="0 0 28 28" fill="none" stroke="#fff" stroke-width="1.5"><circle cx="14" cy="14" r="13" fill="#fff"/><rect x="8" y="9.5" width="12" height="9" rx="1.5" stroke="#000"/><path d="M8 10.5l6 4.5 6-4.5" stroke="#000"/></svg>
  <div class="abs" style="left:169px;top:586px;font-size:11px;color:#ccc">Email Us:</div>
  <div class="abs" style="left:169px;top:603px;font-size:13px;text-decoration:underline">info@velmora.com</div>
  <svg class="abs" style="left:313px;top:589px" width="28" height="28" viewBox="0 0 28 28" fill="none"><circle cx="14" cy="14" r="13" fill="#fff"/><circle cx="14" cy="14" r="6.5" stroke="#000" stroke-width="1.5"/><path d="M14 10.5V14l2.5 1.5" stroke="#000" stroke-width="1.5"/></svg>
  <div class="abs" style="left:350px;top:586px;font-size:11px;color:#ccc">Mon To Sun:</div>
  <div class="abs" style="left:350px;top:603px;font-size:13px">10:00 AM To 6:00 PM</div>

  <div class="abs" style="left:132px;top:663px;width:936px;height:1px;background:#444"></div>
  <div class="abs" style="left:132px;top:708px;font-size:12px;color:#ddd">Copyright @ 2025 Velmora All Rights Reserved</div>
  <div class="abs" style="left:793px;top:708px;font-size:12px;color:#ddd">Privacy Policy &nbsp;|&nbsp; Terms &amp; Conditions &nbsp;|&nbsp; Cookie</div>
</footer>
<div class="social" style="left:903px;background:#fff"></div>
<div class="social" style="left:948px"></div>
<div class="social" style="left:993px"></div>
<div class="social" style="left:1038px"></div>

<section class="contact">
  <h2 class="sec-title" style="top:78px;width:953px;left:0">Contact Us Today</h2>
  <div class="field" style="left:93px;top:169px;width:376px;height:50px">Full name
    <svg width="14" height="14" viewBox="0 0 14 14" fill="none" stroke="#333" stroke-width="1.2"><circle cx="7" cy="4.5" r="3"/><path d="M2 13c0-3 2.2-4.5 5-4.5s5 1.5 5 4.5z"/></svg></div>
  <div class="field" style="left:484px;top:169px;width:376px;height:50px">Email address
    <svg width="15" height="13" viewBox="0 0 15 13" fill="none" stroke="#333" stroke-width="1.2"><rect x="1" y="1.5" width="13" height="10" rx="2"/><path d="M1.5 3l6 4 6-4"/></svg></div>
  <div class="field" style="left:93px;top:235px;width:767px;height:161px;align-items:flex-start;padding-top:20px">Write here message</div>
  <div class="btn" style="left:363px;top:432px;width:227px;height:64px;border-radius:3px;font-family:'Red Hat Display',sans-serif;font-weight:700;font-size:20px">Sent Message</div>
</section>

</body>
</html>
```